Painting Contractor Business Card Design

We are looking for a cool, bold, modern, polished, business card design. We are a high-end residential painting contractor. Please incorporate our logo and keep with our green/black color scheme. We are interested in seeing 2-sided and 1-sided options. Thank you very much!

Industry/Entity Type

Business

Contact Information for Business Card

Info for the card:
Dale Ormsby
mobile 206-555-0193
email dale@tallowbrookpainting.net
web www.tallowbrookpainting.net

```html
<!DOCTYPE html>
<html lang="en">
<head>
<meta charset="utf-8">
<title>Tallowbrook Painting – Business Card</title>
<link href="https://fonts.googleapis.com/css2?family=Montserrat:wght@600&family=Open+Sans:wght@400;700&display=swap" rel="stylesheet">
<style>
  :root {
    --page-bg: #e9ebe8;
    --card-white: #ffffff;
    --brand-green: #3aaa48;
    --brand-green-dark: #223029;
    --brand-green-mid: #3d7447;
    --ink: #111111;
    --text-body: #2a2a2a;
  }
  * { margin: 0; padding: 0; box-sizing: border-box; }
  html, body {
    width: 1200px;
    height: 1200px;
    overflow: hidden;
    background: var(--page-bg);
  }
  .canvas {
    position: relative;
    width: 1200px;
    height: 1200px;
  }
  .card {
    position: absolute;
    left: 160px;
    width: 880px;
    height: 503px;
    overflow: hidden;
    box-shadow: 0 6px 20px rgba(0,0,0,0.18);
  }
  /* ---------- back side ---------- */
  .card-back {
    top: 70px;
    background: linear-gradient(120deg, var(--brand-green-dark) 0%, #2c4a36 45%, var(--brand-green-mid) 100%);
    display: flex;
    align-items: center;
    justify-content: center;
  }
  .back-wordmark {
    font-family: 'Montserrat', sans-serif;
    font-weight: 600;
    font-size: 44px;
    letter-spacing: 3px;
    color: var(--brand-green);
    text-transform: uppercase;
    white-space: nowrap;
  }
  /* ---------- front side ---------- */
  .card-front {
    top: 627px;
    background: var(--card-white);
  }
  .front-shapes {
    position: absolute;
    inset: 0;
    width: 880px;
    height: 503px;
  }
  .holder {
    position: absolute;
    left: 125px;
    top: 34px;
    font-family: 'Open Sans', sans-serif;
    white-space: nowrap;
  }
  .holder-name {
    font-weight: 700;
    font-size: 32px;
    line-height: 1.1;
    color: var(--brand-green);
  }
  .holder-title {
    font-size: 19px;
    color: var(--text-body);
  }
  .contact {
    position: absolute;
    left: 50px;
    top: 196px;
    font-family: 'Open Sans', sans-serif;
    font-size: 17px;
    line-height: 25px;
    color: var(--text-body);
    list-style: none;
    white-space: nowrap;
  }
  .contact .label { color: var(--brand-green); }
  .brand-lockup {
    position: absolute;
    left: 370px;
    top: 226px;
    display: flex;
    align-items: center;
    gap: 14px;
    white-space: nowrap;
  }
  .brand-square {
    flex: none;
    width: 32px;
    height: 32px;
    background: var(--brand-green);
  }
  .brand-name {
    font-family: 'Montserrat', sans-serif;
    font-weight: 600;
    font-size: 26px;
    letter-spacing: 1.5px;
    color: var(--ink);
    text-transform: uppercase;
  }
</style>
</head>
<body>
<main class="canvas">

  <section class="card card-back" aria-label="Business card back">
    <p class="back-wordmark">Tallowbrook Painting</p>
  </section>

  <section class="card card-front" aria-label="Business card front">
    <svg class="front-shapes" viewBox="0 0 880 503" aria-hidden="true">
      <polygon class="top-band" points="0,0 215,0 200,24 0,24" fill="var(--brand-green)"/>
      <polygon class="top-block" points="72,8 112,8 92,52 52,52" fill="var(--ink)"/>
      <polygon class="base-band-green" points="0,398 440,398 420,428 0,428" fill="var(--brand-green)"/>
      <polygon class="base-band-black" points="425,428 880,428 880,490 455,490" fill="var(--ink)"/>
    </svg>

    <div class="holder">
      <p class="holder-name">Dale Ormsby</p>
      <p class="holder-title">Managing Director</p>
    </div>

    <ul class="contact">
      <li>4120 Alder Way South</li>
      <li>Seattle, WA 98108</li>
      <li><span class="label">m:</span> 206-555-0193</li>
      <li><span class="label">w:</span> www.tallowbrookpainting.net</li>
      <li><span class="label">e:</span> dale@tallowbrookpainting.net</li>
    </ul>

    <div class="brand-lockup">
      <span class="brand-square"></span>
      <span class="brand-name">Tallowbrook Painting</span>
    </div>
  </section>

</main>
</body>
</html>
```